Velvet Harbor Tiles Wix Website Design

We are looking for a creative Wix based website design for our new tabletop game and pop-culture collectibles company, Velvet Harbor Tiles. We are looking for something clean, simple, profession and would really like it to be as creative and original as possible. We are trying hard not to be cookie cutter and just use the standard templates. We are attaching our work-in-progress brand guide for reference. Please read though the guide as use the appropriate color pallet and fonts as per the brand guide.

Here are some similar companies in the market for reference and target the same markets as we do.

https://www.brightnook.com/
https://www.parade-fair.org/pfx
http://qz.tollmakers.com/
https://plumtarn.com/
https://www.vostrel.com/
https://www.orchardlanternplay.com/en/index/
http://www.tallpebbleyard.com/
https://www.marlowind.com/games
https://www.haybrickcraft.com/

For illustrative purposes only, please use placeholder images from similar target market websites if necessary but those will be replaced once the design has been established and before publishing.
Updates

Posting our design request during the Christmas holiday season was probably not our best idea as many of our team have not been able to participate in the feedback and evaluation processes. We would like to extend the project 5 more days in order to give the designers proper feedback on the proposals they have submitted rather than just a stars. We WILL be selecting our design choice at the end of this extension. Thanks to everyone who has already submitted. I'm confident we will have something wonderful.

Target Market(s)

Boardgamers, Gamers, Comic Books Fans, ParadeFair attendees, etc.

Number of Pages Required

3 page

Font styles to use
Sans Serif

Colors
000000
ec1f27
ffffff

Requirements
Must have
• See attached Brand Guide for color and logo references. Our company colors are Black / Red / White. Must be WIX compatible. We currently have a place holder landing page setup at www.VelvetHarborTiles.com
Nice to have
• Be creative and original.
Should not have
• no restrictions.... yet. :)

```html
<!DOCTYPE html>
<html lang="en">
<head>
<meta charset="utf-8">
<title>Velvet Harbor Tiles – Article</title>
<link rel="stylesheet" href="https://fonts.googleapis.com/css2?family=Arimo:ital,wght@0,400;0,700;1,400&family=Luckiest+Guy&display=swap">
<style>
:root{
  --red:#ec1f27;
  --black:#000000;
  --white:#ffffff;
  --ink:#1a1a1a;
  --text:#3a3a3a;
  --grey:#8a8a8a;
  --paper:#f4f4f4;
  --band:#e6e6e6;
  --hero:#262626;
  --footer:#1f1f1f;
  --footer-text:#b5b5b5;
}
*{margin:0;padding:0;box-sizing:border-box}
html,body{width:1200px;height:2314px;overflow:hidden}
body{position:relative;font-family:"Arimo",Arial,sans-serif;background:var(--paper);color:var(--text)}
.abs{position:absolute}

/* header */
.site-header{left:0;top:0;width:1200px;height:94px;background:#f7f7f7;box-shadow:0 1px 3px rgba(0,0,0,.25);z-index:3}
.brand-tab{left:108px;top:0;width:148px;height:126px;z-index:4}
.brand-name{left:118px;top:26px;width:128px;text-align:center;z-index:5;font-weight:700;font-size:15px;line-height:18px;color:var(--black);text-transform:uppercase}
.brand-dot{left:170px;top:76px;width:24px;height:24px;background:var(--red);border-radius:50%;z-index:5}
.top-info{top:9px;font-size:9.5px;color:#555;z-index:5;display:flex;align-items:center;gap:6px}
.top-info svg{display:block}
.divider{top:9px;width:1px;height:13px;background:#ccc;z-index:5}
.flag{left:1074px;top:8px;width:22px;height:14px;background:linear-gradient(135deg,#1d3f8f 0 40%,#e9e9ee 40% 60%,#c8102e 60%);z-index:5}
.main-nav{top:56px;z-index:5;font-size:11px;font-weight:700;letter-spacing:.4px;color:var(--ink);text-transform:uppercase}
.cart-btn{left:945px;top:43px;width:148px;height:34px;background:var(--red);color:var(--white);font-size:11px;font-weight:700;text-transform:uppercase;letter-spacing:.4px;display:flex;align-items:center;justify-content:center;z-index:5}

/* hero */
.hero{left:0;top:94px;width:1200px;height:284px;background:radial-gradient(ellipse at 50% 30%,#333 0%,var(--hero) 55%,#1c1c1c 100%)}
.hero-kicker{left:0;top:186px;width:1200px;text-align:center;font-weight:700;font-size:22px;letter-spacing:6px;color:#9a9a9a;text-transform:uppercase}
.hero-title{left:0;top:220px;width:1200px;text-align:center;font-family:"Luckiest Guy",Impact,sans-serif;font-size:60px;color:var(--white);letter-spacing:1px}

/* article */
.article-bg{left:0;top:378px;width:1200px;height:1175px;background:linear-gradient(180deg,#f6f6f6,#efefef)}
.product-shot{left:310px;top:481px;width:261px;height:294px;background:linear-gradient(160deg,#4b6a78 0%,#2e4450 55%,#1b2429 100%);box-shadow:6px 6px 12px rgba(0,0,0,.25)}
.sale-badge{left:306px;top:493px;width:62px;height:62px}
.sale-text{left:306px;top:510px;width:62px;text-align:center;color:var(--white);font-weight:700;font-size:15px;line-height:13px}
.sale-text small{font-size:8px}
.lead-title{left:606px;top:502px;width:330px;font-weight:700;font-size:24px;line-height:27px;color:var(--black)}
.lead-copy{left:608px;top:574px;width:330px;font-size:13px;line-height:29px;color:var(--text)}
.section-title{left:336px;top:836px;font-weight:700;font-size:23px;color:var(--black)}
.body-copy{width:600px;font-size:13.5px;line-height:30.5px;color:var(--text)}
.quote-mark{left:272px;top:1132px;font-family:Georgia,serif;font-size:62px;color:var(--red);font-style:italic;line-height:1}
.pull-quote{left:338px;top:1124px;width:600px;font-style:italic;font-size:25px;line-height:31px;color:var(--ink)}

/* similar articles */
.similar-band{left:0;top:1553px;width:1200px;height:487px;background:linear-gradient(180deg,#e9e9e9,#e2e2e2);border-top:1px solid #d2d2d2}
.similar-title{left:0;top:1621px;width:1200px;text-align:center;font-family:"Luckiest Guy",Impact,sans-serif;font-size:36px;color:#333}
.similar-sub{left:0;top:1666px;width:1200px;display:flex;justify-content:center;align-items:center;gap:12px;font-weight:700;font-size:15px;color:#666;letter-spacing:.3px}
.similar-sub i{display:block;width:30px;height:2px;background:#888}
.slider-arrows{left:998px;top:1664px}
.card{top:1729px;width:451px;height:239px;background:#f8f8f8;box-shadow:0 1px 4px rgba(0,0,0,.12)}
.card-shot{left:41px;top:37px;width:132px;height:162px;background:linear-gradient(160deg,#4b6a78 0%,#2e4450 55%,#1b2429 100%);box-shadow:4px 4px 8px rgba(0,0,0,.25)}
.card-title{left:217px;top:48px;font-family:"Luckiest Guy",Impact,sans-serif;font-size:22px;color:#222}
.card-copy{left:219px;top:88px;width:195px;font-size:10.5px;line-height:17px;color:#333}
.card-btn{left:219px;top:175px;width:92px;height:24px;background:var(--red);color:var(--white);font-weight:700;font-size:8.5px;display:flex;align-items:center;justify-content:center}

/* footer */
.site-footer{left:0;top:2040px;width:1200px;height:274px;background:var(--footer)}
.footer-col{top:2086px}
.footer-col h3{font-family:"Luckiest Guy",Impact,sans-serif;font-weight:400;font-size:15px;color:var(--white);letter-spacing:.5px;margin-bottom:10px}
.footer-col li{list-style:none;font-size:12px;line-height:25.7px;color:var(--footer-text)}
.email-field{left:874px;top:2123px;width:153px;height:25px;background:#e9e9e9;border:1px solid #bbb;font-size:9.5px;color:#666;padding:6px 8px}
.submit-btn{left:874px;top:2157px;width:65px;height:22px;background:var(--red);color:var(--white);font-weight:700;font-size:9px;display:flex;align-items:center;justify-content:center}
.footer-rule{left:0;top:2276px;width:1200px;height:1px;background:#333}
.legal{left:182px;top:2288px;font-size:8.5px;color:#9a9a9a}
.social{left:924px;top:2286px;display:flex;gap:8px}
.social i{display:block;width:14px;height:14px;border-radius:50%;background:#8d8d8d}
</style>
</head>
<body>

<header class="site-header abs"></header>
<svg class="brand-tab abs" width="148" height="126" viewBox="0 0 148 126" aria-hidden="true">
  <path d="M0 94 Q22 94 32 110 Q48 126 74 126 Q100 126 116 110 Q126 94 148 94 L148 0 L0 0 Z" fill="#f7f7f7"/>
</svg>
<div class="brand-name abs">Velvet Harbor Tiles</div>
<div class="brand-dot abs"></div>

<div class="top-info abs" style="left:598px">
  <svg width="16" height="12" viewBox="0 0 16 12"><rect x="0" y="1" width="10" height="7" fill="#666"/><path d="M10 3h3l3 3v2h-6z" fill="#666"/><circle cx="3.5" cy="10" r="1.6" fill="#666"/><circle cx="12.5" cy="10" r="1.6" fill="#666"/></svg>
  <span>Free Shipping over $50</span>
</div>
<div class="divider abs" style="left:753px"></div>
<div class="top-info abs" style="left:777px">
  <svg width="12" height="9" viewBox="0 0 12 9"><rect width="12" height="9" fill="#666"/><path d="M0 0l6 5 6-5" stroke="#f7f7f7" fill="none"/></svg>
  <span>hello@velvetharbortiles.com</span>
</div>
<div class="divider abs" style="left:946px"></div>
<div class="top-info abs" style="left:966px">
  <svg width="10" height="10" viewBox="0 0 10 10"><path d="M2 0l2 2.5-1.2 1.5a6 6 0 0 0 3.2 3.2L7.5 6 10 8l-1.5 2C4 10 0 6 0 1.5z" fill="#666"/></svg>
  <span>555 014 2290</span>
</div>
<div class="flag abs" role="img" aria-label="Language flag"></div>

<nav>
  <div class="main-nav abs" style="left:412px">About Us</div>
  <div class="main-nav abs" style="left:540px">How to Play</div>
  <div class="main-nav abs" style="left:683px">Contact Us</div>
  <div class="main-nav abs" style="left:821px">My Orders</div>
</nav>
<div class="cart-btn abs">Add to Cart</div>

<section>
  <div class="hero abs"></div>
  <div class="hero-kicker abs">Secondary Headline</div>
  <h1 class="hero-title abs">Article Headline</h1>
</section>

<main>
  <div class="article-bg abs"></div>
  <div class="product-shot abs" role="img" aria-label="Boxed tabletop game with sci-fi crew artwork"></div>
  <svg class="sale-badge abs" viewBox="0 0 62 62" aria-hidden="true">
    <polygon fill="#ec1f27" points="31,0 37,10 48,5 48,17 60,19 53,29 62,38 50,42 52,54 40,51 33,62 26,52 14,57 14,45 2,42 9,32 0,23 12,19 11,7 23,11"/>
  </svg>
  <div class="sale-text abs">10%<br><small>LESS</small></div>

  <h2 class="lead-title abs">Some kind of starting paragraph sentences</h2>
  <p class="lead-copy abs">Lorem ipsum dolor sit amet, consectetuer adipi-scing elit. Aenean commodo ligula eget dolor. Aenean massa. Cum sociis natoque penatibus et magnis dis parturient montes, nascetur ridicu-lus mus. Donec quam felis, ultricies nec, pellen-tesque eu, pretium quis,</p>

  <h2 class="section-title abs">Some kind of starting paragraph.</h2>
  <p class="body-copy abs" style="left:335px;top:882px">Lorem ipsum dolor sit amet, consectetuer adipiscing elit. Aenean commodo ligula eget dolor. Aenean massa. Cum sociis natoque penatibus et magnis dis parturient montes, nascetur ridiculus mus. Donec quam felis, ultricies nec,</p>
  <p class="body-copy abs" style="left:335px;top:986px">Lorem ipsum dolor sit amet, consectetuer adipiscing elit. Aenean commodo ligula eget dolor. Aenean massa. Cum sociis natoque penatibus et magnis dis parturient montes, nascetur ridiculus mus. Donec quam felis, ultricies nec</p>

  <div class="quote-mark abs">“</div>
  <blockquote class="pull-quote abs">Lorem ipsum dolor sit amet, cosectetuer adipisc scing elit commodo ligula eget</blockquote>

  <p class="body-copy abs" style="left:330px;top:1223px">Lorem ipsum dolor sit amet, consectetuer adipiscing elit. Aenean commodo ligula eget dolor. Aenean massa. Cum sociis natoque penatibus et magnis dis parturient montes, nascetur ridiculus mus. Donec quam felis, ultricies nec,</p>
  <p class="body-copy abs" style="left:330px;top:1330px">Lorem ipsum dolor sit amet, consectetuer adipiscing elit. Aenean commodo ligula eget dolor. Aenean massa. Cum sociis natoque penatibus et magnis dis parturient montes, nascetur ridiculus mus. Donec quam felis, ultricies nec</p>
</main>

<section>
  <div class="similar-band abs"></div>
  <h2 class="similar-title abs">Similar Articles</h2>
  <div class="similar-sub abs"><i></i>About Newest Products<i></i></div>
  <svg class="slider-arrows abs" width="56" height="24" viewBox="0 0 56 24" aria-hidden="true">
    <path d="M22 12H3M10 5L3 12l7 7" stroke="#222" stroke-width="2.2" fill="none"/>
    <path d="M34 12h19M46 5l7 7-7 7" stroke="#999" stroke-width="2" fill="none"/>
  </svg>

  <article class="card abs" style="left:139px">
    <div class="card-shot abs" role="img" aria-label="Boxed tabletop game with sci-fi crew artwork"></div>
    <h3 class="card-title abs">Article Headline</h3>
    <p class="card-copy abs">Lorem ipsum dolor sit amet, consec-tetuer adipiscing elit. Aenean commo-do magnis dis parturient montes, na-scetur ridiculus mus.</p>
    <div class="card-btn abs">Read Article</div>
  </article>
  <article class="card abs" style="left:606px">
    <div class="card-shot abs" role="img" aria-label="Boxed tabletop game with sci-fi crew artwork"></div>
    <h3 class="card-title abs">Article Headline</h3>
    <p class="card-copy abs">Lorem ipsum dolor sit amet, consec-tetuer adipiscing elit. Aenean commo-do magnis dis parturient montes, na-scetur ridiculus mus.</p>
    <div class="card-btn abs">Read Article</div>
  </article>
</section>

<footer>
  <div class="site-footer abs"></div>
  <div class="footer-col abs" style="left:182px">
    <h3>Navigation</h3>
    <ul><li>Who we are</li><li>What we do</li><li>Features</li><li>Architecture</li><li>Core Team</li></ul>
  </div>
  <div class="footer-col abs" style="left:412px">
    <h3>Policy</h3>
    <ul><li>Conditions &amp; Terms</li><li>About us</li><li>Privacy Policy</li><li>Write to us</li><li>Block Securtiy</li></ul>
  </div>
  <div class="footer-col abs" style="left:648px">
    <h3>Contacts</h3>
    <ul><li>Your Street Adress</li><li>Phone Numbers</li><li>Email Addresses</li><li>Working Hours</li><li>Products</li></ul>
  </div>
  <div class="footer-col abs" style="left:876px">
    <h3>Subscribe</h3>
  </div>
  <div class="email-field abs">Email Address</div>
  <div class="submit-btn abs">Submit</div>
  <div class="footer-rule abs"></div>
  <div class="legal abs">Conditions &amp; Terms &nbsp;|&nbsp; Privacy Policy &nbsp;|&nbsp; All rights reserved 2018</div>
  <div class="social abs" aria-label="Social links"><i></i><i></i><i></i><i></i><i></i></div>
</footer>

</body>
</html>
```